Design a modern, classy & professional business card for an online real estate agency, specializing in medium-luxury properties in Thailand and later in Singapore and UK.

Possible design ideas so far: (not essential)

- curved corner(s) to the card, white on front & turquoise on back or visa versa.

- front of card - clear and simple, company name in metallic grey/monochrome, logo graphic & company name on front in spot UV or embossed/debossed effect.

- back of card - large, close-cropped, 'ghost' patterns of the C-shaped curves of logo, or company name repeated on back of card in spot UV.

Target Market(s)

- young to middle-aged professionals mainly (but ideally should design should suit all)

- UK, US,EU,AUS & ASIAN mainly (but ideally should design should suit all countries)

Industry/Entity Type

Real Estate

Requirements
Must have
• THEME:
- Luxurious & Modern
- Clean & striking
- Unique & creative

INFO:
- Logo & company name on front
- Contact details on back:

Tobias Lindqvist
Managing Director

www.velmoraestates.example
www.velmoraestates-uk.example

Tel: 083-274-6190
email: tobias@velmoraestates.example

(contact details can be displayed in any order as suites design.)

Nice to have
• - curved corner(s) to the card, white on front & turquoise on back or visa versa.

Should not have
• - No generic images of properties, palm trees/coconut trees etc.

- No other other bold colors, except for main turquoise, grey, metallic white & black theme.

- No obvious business card templates

```html
<!DOCTYPE html>
<html lang="en">
<head>
<meta charset="utf-8">
<title>Velmora Estates — Business Card</title>
<link rel="stylesheet" href="https://fonts.googleapis.com/css2?family=Arimo&family=EB+Garamond&family=Tinos&display=swap">
<style>
  :root {
    --backdrop: #b3b3b3;
    --card: #2f2c2c;
    --band: #050505;
    --stripe: #4b4848;
    --turquoise: #1cc6c4;
    --brand-grey: #8e8e8e;
    --name-grey: #ababab;
    --white: #ffffff;
    --rule: #8a8787;
  }
  html, body {
    margin: 0;
    width: 1200px;
    height: 888px;
    overflow: hidden;
    background: var(--backdrop);
  }
  .sheet { display: block; width: 1200px; height: 888px; }
  .card-shape { fill: var(--card); }
  .front-band { fill: var(--band); }
  .front-stripe { fill: var(--stripe); }
  .brand-square { fill: var(--turquoise); }
  .brand-name {
    font-family: "EB Garamond", serif;
    fill: var(--brand-grey);
    font-weight: 400;
  }
  .brand-sub { letter-spacing: 5px; }
  .holder-name {
    font-family: "Arimo", sans-serif;
    font-size: 38px;
    fill: var(--name-grey);
  }
  .holder-role {
    font-family: "Tinos", serif;
    font-size: 25px;
    fill: var(--white);
    letter-spacing: 0.5px;
  }
  .contact {
    font-family: "Arimo", sans-serif;
    font-size: 17px;
    fill: var(--white);
  }
  .contact-rule { stroke: var(--rule); stroke-width: 1.2; }
</style>
</head>
<body>
<svg class="sheet" viewBox="0 0 1200 888" xmlns="http://www.w3.org/2000/svg">
  <defs>
    <clipPath id="front-clip">
      <path d="M84,168 A130,130 0 0 1 214,38 H792 V312 A130,130 0 0 1 662,442 H84 Z"/>
    </clipPath>
  </defs>

  <!-- Front of card -->
  <g class="card-front">
    <path class="card-shape" d="M84,168 A130,130 0 0 1 214,38 H792 V312 A130,130 0 0 1 662,442 H84 Z"/>
    <g clip-path="url(#front-clip)">
      <rect class="front-stripe" x="84" y="138" width="708" height="10"/>
      <rect class="front-band" x="84" y="148" width="708" height="185"/>
      <rect class="front-stripe" x="84" y="333" width="708" height="11"/>
    </g>
    <rect class="brand-square" x="226" y="181" width="120" height="120"/>
    <text class="brand-name" x="356" y="262" font-size="78">Velmora</text>
    <text class="brand-name brand-sub" x="366" y="294" font-size="26">ESTATES</text>
  </g>

  <!-- Back of card -->
  <g class="card-back">
    <path class="card-shape" d="M425,553 A130,130 0 0 1 555,423 H1133 V698 A130,130 0 0 1 1003,828 H425 Z"/>
    <rect class="brand-square" x="761" y="461" width="90" height="90"/>
    <text class="brand-name" x="862" y="522" font-size="60">Velmora</text>
    <text class="brand-name brand-sub" x="868" y="546" font-size="20">ESTATES</text>

    <text class="holder-name" x="790" y="645" text-anchor="middle">Tobias Lindqvist</text>
    <text class="holder-role" x="779" y="680" text-anchor="middle">Managing Director</text>

    <line class="contact-rule" x1="463" y1="735" x2="1066" y2="735"/>
    <text class="contact" x="466" y="763">Tel&#160;&#160;&#160;&#160;: 083-274-6190</text>
    <text class="contact" x="466" y="786">email : tobias@velmoraestates.example</text>
    <text class="contact" x="1066" y="763" text-anchor="end">www.velmoraestates.example</text>
    <text class="contact" x="1066" y="786" text-anchor="end">www.velmoraestates-uk.example</text>
    <line class="contact-rule" x1="463" y1="800" x2="1066" y2="800"/>
  </g>
</svg>
</body>
</html>
```